pet sitting business brochure

please create a professional bold brochure for my new pet sitting business
please use my logo and collect suitable photos online to go with design of brochure
my colour theme is orange and blue
please look at my website to collect information
www.kestrelpawminders.com.au

Reason: extended until tomorrow to make any changes to designs

```html
<!DOCTYPE html>
<html lang="en">
<head>
<meta charset="utf-8">
<title>Kestrel Paw Minders – Brochure</title>
<link href="https://fonts.googleapis.com/css2?family=Open+Sans:ital,wght@0,400;0,600;0,700;1,400;1,600&display=swap" rel="stylesheet">
<style>
:root{
  --blue:#4a86c8;
  --blue-light:#7aa8dc;
  --orange:#e8862a;
  --white:#ffffff;
  --page:#ffffff;
  --ink:#111111;
}
*{box-sizing:border-box;margin:0;padding:0}
html,body{width:1200px;height:900px;overflow:hidden;background:var(--page)}
body{position:relative;font-family:"Open Sans",Arial,sans-serif}
.view-label{position:absolute;left:0;width:1200px;text-align:center;font-size:50px;font-weight:400;color:var(--ink);line-height:1}
.view-label--outside{top:14px}
.view-label--inside{top:458px}
.spread-frame{position:absolute;left:358px;width:484px;height:374px}
.spread-frame--outside{top:74px}
.spread-frame--inside{top:520px}
.spread{position:absolute;left:0;top:0;width:440px;height:340px;transform:scale(1.1);transform-origin:0 0;background:var(--white);overflow:hidden;box-shadow:0 0 0 .5px #ddd}
.spread svg.bands{position:absolute;left:0;top:0;width:440px;height:340px}
.photo{position:absolute;border-radius:50%;border:4px solid var(--orange)}
.photo--flat{border-radius:0;border:none}
.badge{position:absolute;border-radius:50%;background:var(--white);border:3px solid var(--orange);display:flex;align-items:center;justify-content:center;text-align:center}
.badge p{font-size:7.5px;line-height:1.3;font-weight:700;color:var(--blue)}
.badge--italic p{font-style:italic;font-weight:600;color:var(--blue);font-size:10px}
.badge--orange p{color:var(--orange);font-style:italic;font-weight:600;font-size:8.5px}
.heading{position:absolute;font-weight:700;line-height:1;white-space:nowrap}
.heading--orange{color:var(--orange)}
.heading--blue{color:var(--blue)}
.block{position:absolute;font-size:4.8px;line-height:1.35;text-align:center}
.block h4{font-size:6px;font-weight:700;margin-top:5px;line-height:1.2}
.block--orange{color:var(--orange)}
.block--blue{color:var(--blue)}
.copy{position:absolute;font-size:5px;line-height:1.5}
.copy p{margin-bottom:6px}
.copy--blue{color:var(--blue)}
.copy--orange{color:var(--orange);text-align:center}
.contact{position:absolute;left:155px;top:175px;color:var(--blue)}
.contact h3{font-size:17px;font-weight:700;line-height:1;margin-bottom:5px}
.contact p{font-size:6.5px;line-height:1.4}
.brand{position:absolute;left:292px;top:10px;width:130px;height:130px;border-radius:50%;background:var(--white);display:flex;flex-direction:column;align-items:center;justify-content:center;text-align:center}
.brand-mark{width:14px;height:14px;border-radius:50%;background:var(--blue);margin-bottom:6px}
.brand-name{font-size:11px;font-weight:700;color:var(--blue);line-height:1.15}
</style>
</head>
<body>

<h2 class="view-label view-label--outside">Outside</h2>
<div class="spread-frame spread-frame--outside">
  <section class="spread spread--outside">
    <div class="photo photo--flat" role="img" aria-label="Close-up photo of a beagle puppy in autumn leaves" style="left:115px;top:140px;width:325px;height:200px;background:radial-gradient(circle at 65% 60%,#e9e2d6 0%,#a9804e 35%,#6c4a2a 70%,#3b2817 100%)"></div>
    <svg class="bands" viewBox="0 0 440 340" aria-hidden="true">
      <path d="M0 0H440V70C360 90 250 50 150 75C90 90 40 90 0 95Z" fill="var(--blue)"/>
      <path d="M0 95C40 90 90 90 150 75C250 50 360 90 440 70V140C370 170 260 120 160 160C100 180 40 170 0 165Z" fill="var(--orange)"/>
      <path d="M0 165C40 170 100 180 160 160C150 200 125 280 115 340H0Z" fill="var(--white)"/>
      <path d="M0 165C40 170 100 180 160 160" fill="none" stroke="var(--blue)" stroke-width="3"/>
      <circle cx="360" cy="30" r="40" fill="none" stroke="var(--blue-light)" stroke-width=".6"/>
      <circle cx="210" cy="20" r="30" fill="none" stroke="var(--blue-light)" stroke-width=".6"/>
    </svg>
    <div class="photo" role="img" aria-label="Photo of a brown horse in a paddock" style="left:-5px;top:12px;width:90px;height:148px;border-radius:0 80px 80px 0;background:linear-gradient(160deg,#7f9a5a,#5a3a22 55%,#3a5a2a)"></div>
    <div class="badge" style="left:175px;top:45px;width:80px;height:80px"><p>More than<br>4 pets?<br>No Problem!<br>Contact us<br>for a quote<br>now!</p></div>
    <div class="brand"><span class="brand-mark"></span><span class="brand-name">KESTREL<br>PAW MINDERS</span></div>
    <div class="badge" style="left:362px;top:118px;width:80px;height:80px"><p style="color:var(--orange);font-weight:600">We offer a<br>professional<br>and caring pet<br>sitting service<br>to the<br>Myrtle Valley.</p></div>
    <h2 class="heading heading--orange" style="left:36px;top:168px;font-size:18px">Prices</h2>
    <div class="block block--orange" style="left:12px;top:186px;width:100px;font-size:5px">
      <h4>Pet Sitting</h4>
      <div>Once Daily visit<br>1 - 2 Pets: $25<br>3 - 4 Pets: $30<br>More: Ask for quote<br>Twice Daily Visit<br><br>1 - 2 Pets: $40<br>3 - 4 Pets: $45<br>More: Ask for quote</div>
      <h4>Dog Walking</h4>
      <div>20 minutes - $20<br>40 minutes - $30<br>60 minutes - $45</div>
      <h4>Additional Services:</h4>
      <div>Horses Rugged: $5 - $15<br>Medicine Administration: $5<br>Plant Watering: $5- $15</div>
    </div>
    <div class="contact">
      <h3>Contact Us</h3>
      <p>Mobile: 0400 123 456<br>Email: maya@kestrelpawminders.com.au<br>www.kestrelpawminders.com.au</p>
    </div>
    <div class="photo" role="img" aria-label="Photo of a black and tan puppy" style="left:103px;top:240px;width:96px;height:96px;background:radial-gradient(circle at 50% 55%,#5a3a22,#1e1510 70%)"></div>
  </section>
</div>

<h2 class="view-label view-label--inside">Inside</h2>
<div class="spread-frame spread-frame--inside">
  <section class="spread spread--inside">
    <svg class="bands" viewBox="0 0 440 340" aria-hidden="true">
      <path d="M0 0H440V48C380 56 320 44 260 52C180 62 100 52 0 56Z" fill="var(--blue)"/>
      <circle cx="290" cy="22" r="30" fill="none" stroke="var(--white)" stroke-width=".6"/>
      <circle cx="400" cy="35" r="25" fill="none" stroke="var(--white)" stroke-width=".6"/>
      <path d="M0 330C120 327 300 333 440 322V340H0Z" fill="var(--orange)"/>
      <path d="M0 327C120 324 300 330 440 319" fill="none" stroke="var(--blue)" stroke-width="1.5"/>
    </svg>
    <div class="photo" role="img" aria-label="Photo of a brown rabbit" style="left:-5px;top:-5px;width:130px;height:123px;border-radius:0 0 100px 0;background:radial-gradient(circle at 60% 55%,#d1a57a,#8a5e3a 55%,#3e2a1a)"></div>
    <div class="badge badge--italic" style="left:96px;top:8px;width:76px;height:76px"><p>We care<br>for all<br>kinds of<br>pets</p></div>
    <h2 class="heading heading--orange" style="left:174px;top:79px;font-size:17px">About Us</h2>
    <div class="copy copy--orange" style="left:157px;top:104px;width:165px">
      <p>Hi, my name is Maya and I'm a fully qualified animal technician, with over 12 years experience in caring for all kinds of animals. I also hold a Diploma in Animal Technology and a Bachelor of Applied Science.</p>
      <p>I pride myself in providing a high professional standard of care and, combined with my soft-hearted nature and skills I've learnt over the years, I will offer your animals the love and care they deserve while you're away from home.</p>
      <p>If you're looking for a pet sitter to look after your animals in the comfort of your own home, who is professional, qualified and loves animals then give me a call.</p>
    </div>
    <div class="copy copy--blue" style="left:12px;top:142px;width:118px">
      <p>Kestrel Paw Minders offers a professional and caring pet sitting service to the Myrtle Valley.</p>
      <p>We will visit your home to care for your pet in the comfort of their own environment.</p>
      <p>We also offer a dog walking service for owners who are too busy or if you would like your dog exercised while you're away from home to keep them entertained and happy.</p>
      <p style="width:46px">We care for all kinds of pets including horses, livestock, cats, dogs, rodents, birds, fish, and reptiles.</p>
    </div>
    <div class="photo" role="img" aria-label="Photo of a kitten playing with a toy" style="left:62px;top:234px;width:104px;height:104px;background:radial-gradient(circle at 50% 50%,#d9b48a,#9a7a5a 55%,#6a8a5a)"></div>
    <div class="badge badge--orange" style="left:226px;top:268px;width:68px;height:68px"><p>We come<br>to your pet<br>in your<br>home.</p></div>
    <div class="photo" role="img" aria-label="Photo of a woman walking a dog on a path" style="left:342px;top:-5px;width:103px;height:102px;border-radius:0 0 0 60px;background:linear-gradient(170deg,#6a8a4a,#8c6fa8 45%,#c8b89a)"></div>
    <h2 class="heading heading--blue" style="left:323px;top:110px;font-size:17px">Services</h2>
    <div class="block block--blue" style="left:303px;top:126px;width:134px">
      <h4>Pet Sitting</h4>
      <div>We come to your pet in your home. Includes:<br>Feeding<br>Water checked<br>Play time<br>Poop removal<br>Mail Collected<br>Bins taken in or out</div>
      <h4>Dog Walking</h4>
      <div>Feel guilty that your dog is sitting at home alone all day long? While your away from home or at work? Let me spoil your pooch in your absence with a great dog walk!<br><br>Professional Dog Walking is the core of all pet care. Daily dog walking provides a dog with a positive and healthy outlook towards its surroundings. Daily exercise helps to maintain or develop a dog's good temperament.</div>
      <h4>Additional Services:</h4>
      <div>Horses Rugged : Price charged on number of horses and ease of catching<br>Plants Watered : Price charged on number of plants and time spent<br>Medicine Administered : charged daily</div>
    </div>
  </section>
</div>

</body>
</html>
```